Create professional business cards using the attached logo previously designed using BrightPitch. Would like to see a business card that stands out from the crowd.

One side should just have our logo and our business name ie Lamppost Guidance Partners, and the other side should have a smaller version of logo and company name, but together with our business details detailed below. Two cards will need to be produced for myself and my business partner

Professional financial advice to streetlighting engineers and finance people.

Business

The business card will need to contain; name, title (ie Director, email, mobile number, and website address.

• HoratioB and HoratioM

• We would like modern clean looking professional business cards that incorprates the attached .ai file logo. Font used is HoratioB and HoratioM and the name of the company is Lamppost Guidance Partners.
• One side should just have our logo and our business name ie Lamppost Guidance Partners, and the other side should have a smaller version of logo and company name, but together with our business details as above.
• We would potentially like to emboss the logo and name Lamppost Guidance Partners Ltd. Perhaps something that reflects the transition from night to day eg white on one side, black on the other.
• We are open minded. Do not want anything that would appear as a stock copy and paste from a 'normal' business card website eg CardMorrow

```html
<!DOCTYPE html>
<html lang="en">
<head>
<meta charset="utf-8">
<title>Lamppost Guidance Partners – Business Cards</title>
<link href="https://fonts.googleapis.com/css2?family=Jost:wght@400;500&display=swap" rel="stylesheet">
<style>
  :root {
    --backdrop: #8e908f;
    --card: #ebebed;
    --ink: #141414;
    --accent: #c0266a;
  }
  * { margin: 0; padding: 0; box-sizing: border-box; }
  html, body { width: 1200px; height: 900px; overflow: hidden; }
  body {
    position: relative;
    background: var(--backdrop);
    font-family: "Jost", "Futura", sans-serif;
    color: var(--ink);
  }
  .card {
    position: absolute;
    width: 289px;
    height: 522px;
    background: var(--card);
  }
  .card--details { left: 229px; top: 115px; }
  .card--brand { left: 623px; top: 239px; }

  .mark-small {
    position: absolute;
    left: 33px;
    top: 58px;
    display: flex;
    align-items: center;
    gap: 8px;
    font-size: 12px;
    font-weight: 500;
    letter-spacing: 0.02em;
  }
  .mark-square {
    width: 14px;
    height: 14px;
    background: var(--accent);
  }

  .person-name {
    position: absolute;
    left: 33px;
    top: 226px;
    font-size: 24px;
    font-weight: 500;
  }
  .person-title {
    position: absolute;
    left: 33px;
    top: 261px;
    font-size: 13px;
    text-transform: uppercase;
  }
  .contact {
    position: absolute;
    left: 33px;
    top: 314px;
    list-style: none;
    font-size: 13px;
    line-height: 19px;
  }
  .company-name {
    position: absolute;
    left: 33px;
    top: 432px;
    font-size: 23px;
    line-height: 28px;
    font-weight: 500;
    text-transform: uppercase;
  }

  .brand-lockup {
    position: absolute;
    left: 0;
    right: 0;
    top: 190px;
    display: flex;
    flex-direction: column;
    align-items: center;
    gap: 18px;
    text-align: center;
  }
  .brand-lockup .mark-square { width: 34px; height: 34px; }
  .brand-name {
    font-size: 24px;
    line-height: 30px;
    font-weight: 500;
    text-transform: uppercase;
  }
</style>
</head>
<body>
  <section class="card card--details">
    <div class="mark-small"><span class="mark-square"></span>Lamppost Guidance Partners</div>
    <h1 class="person-name">Elena Marsh</h1>
    <p class="person-title">Director</p>
    <ul class="contact">
      <li>+1 555 014 272</li>
      <li>elena@lamppostguidance.com</li>
      <li>www.lamppostguidance.com</li>
    </ul>
    <p class="company-name">Lamppost Guidance<br>Partners</p>
  </section>

  <section class="card card--brand">
    <div class="brand-lockup">
      <span class="mark-square"></span>
      <p class="brand-name">Lamppost<br>Guidance<br>Partners</p>
    </div>
  </section>
</body>
</html>
```